Medical Centre Trifold Brochure

New Medical Centre needs a bright and airy Trifold brochure. We want to introduce our practice to the surrounding area so want to advise our services and introduce the Doctors and Nurses.

I will upload all the pictures and logos, along with some pdf pages of styles that we like (and some we dont) to assist your creativity.

We will provide as much feedback for you as possible.

After this project, we would like to work with the same designer to expand into some other brochures etc that we have in mind, so this is a starting point.
Updates

Hi Designers,

We are looking forward to seeing yuor work. Are you happy that you have enough information to get started?

Please let me know if you need anything else?

Cheers

Hi Designers.. I should mention the brochure itself.. we are looking for a doubled sided, full colour brochure that will be folded into thirds so it becomes a DL size.. I hope that makes sense.

Any questions always welcome.

Target Market(s)

Females - Mothers / Wives / Grandmothers

Industry/Entity Type

Medical

Requirements
Must have
• Tri Fold Medical – Tallowby Family Health

• Include images of the Doctors (I will supply) and the Nursing Staff

• “Chunks” of information
o Introduction to who we are (I will supply)
o Our services (I will supply)
o Fee’s
• We are a newly renovated Medical Clinic
• Google Map of our location – Photo of the outside of the centre near the google map
• Opening Hours
• Contact Details / website address www.tallowbyfamilyhealth.com.au (not yet live but must be included)
• Interior Reception area photo
• Ask a question.. “Are you worried about your patient history?.. We can help”
• Need to leave a space for a Magnet.. (business card sized)

3 Doctor Photos (2 uploaded already)
Image of the centre (uploaded already)

I will upload a detailed description of what we are looking for.
Nice to have
• Photo's of 2 Nurses (1 already uploaded - Maren)

```html
<!DOCTYPE html>
<html lang="en">
<head>
<meta charset="utf-8">
<title>Tallowby Family Health – Trifold Brochure</title>
<link href="https://fonts.googleapis.com/css2?family=Arimo:ital,wght@0,400;0,700;1,700&display=swap" rel="stylesheet">
<style>
  :root{
    --backdrop:#9b9b9d;
    --sheet:#ffffff;
    --green-dark:#4a8a2f;
    --green:#5cb23a;
    --green-light:#8cc63f;
    --lime:#c8dc2a;
    --yellow:#f4ee2a;
    --red:#e3231c;
    --orange:#f07d1b;
    --text:#3e3e3e;
    --grey-text:#8a8b8d;
    --magnet:#e6e7e8;
  }
  *{box-sizing:border-box;margin:0;padding:0}
  html,body{width:1200px;height:900px;overflow:hidden;background:var(--backdrop)}
  body{font-family:"Arimo",Arial,sans-serif;color:var(--text);position:relative}
  .sheet{position:absolute;left:37px;top:48px;width:1128px;height:800px;background:var(--sheet);overflow:hidden}
  .artwork{position:absolute;left:0;top:0}
  .abs{position:absolute}

  .heading{color:var(--green-dark);font-weight:700;text-transform:uppercase}
  .about-title{left:21px;top:45px;font-size:26px}
  .body-copy{font-size:10px;line-height:18.3px;color:var(--text)}
  .about-p1{left:21px;top:88px;width:350px}
  .about-p2{left:21px;top:216px;width:350px}

  .question{left:400px;top:57px;width:243px;height:130px}
  .question-text{left:400px;top:84px;width:243px;text-align:center;color:#fff;font-weight:700;font-size:17px;line-height:22px}

  .doctor-card{position:absolute;width:346px;height:160px;border:3px solid var(--green);border-radius:14px;overflow:hidden;background:#fff;display:flex}
  .doctor-photo{width:148px;height:100%;background:linear-gradient(180deg,#eeeeee 0%,#d9d9d9 55%,#8d8f8c 100%)}
  .doctor-info{flex:1;background:linear-gradient(90deg,var(--green-light),var(--green));padding:9px 10px 0;text-align:center;color:#fff}
  .doctor-name{color:var(--yellow);font-style:italic;font-weight:700;font-size:16px;text-transform:uppercase;margin-bottom:4px}
  .doctor-bio{font-size:10px;line-height:15.8px}
  .card-a{left:390px;top:206px}
  .card-b{left:390px;top:390px}
  .card-b .doctor-info{flex:0 0 193px}
  .card-b .doctor-photo{flex:1}
  .card-c{left:758px;top:206px}
  .doctor-name.mixed{text-transform:none}

  .middle-p{left:390px;top:569px;width:350px}

  .brand{right:30px;top:30px;display:flex;align-items:center;gap:8px;width:150px}
  .brand-mark{width:20px;height:20px;background:var(--green-light);flex:none}
  .brand-name{color:var(--green-dark);font-size:18px;font-weight:700;line-height:21px}

  .tagline{left:771px;top:145px;color:var(--red);font-weight:700;font-size:18px}
  .doctors-title{left:771px;top:170px;font-size:24px}

  .services-title{left:771px;top:380px;font-size:16px}
  .services-p{left:771px;top:402px;width:170px;font-size:9.5px;line-height:18.3px}
  .service-list{left:960px;top:418px;list-style:none}
  .service-list li{display:flex;align-items:center;gap:10px;color:var(--orange);font-weight:700;font-size:16px;height:26px}
  .service-list li::before{content:"";width:15px;height:15px;border-radius:50%;background:radial-gradient(circle,var(--lime) 35%,var(--green-light) 70%)}

  .magnet{left:758px;top:540px;width:346px;height:211px;border-radius:8px;background:rgba(230,231,232,.88);text-align:center;padding-top:68px;color:var(--grey-text);font-style:italic;font-weight:700;font-size:16px;line-height:24.5px}
</style>
</head>
<body>
<main class="sheet">
  <svg class="artwork" width="1128" height="800" viewBox="0 0 1128 800" aria-hidden="true">
    <defs>
      <linearGradient id="bandGrad" x1="0" y1="0" x2="1" y2="0">
        <stop offset="0" stop-color="#8cc63f"/><stop offset=".5" stop-color="#c8dc2a"/><stop offset="1" stop-color="#6cb33f"/>
      </linearGradient>
      <linearGradient id="swooshGrad" x1="0" y1="1" x2="1" y2="0">
        <stop offset="0" stop-color="#4fa634"/><stop offset=".6" stop-color="#8cc63f"/><stop offset="1" stop-color="#c8dc2a"/>
      </linearGradient>
      <linearGradient id="bubbleGrad" x1="0" y1="0" x2="0" y2="1">
        <stop offset="0" stop-color="#f7b21a"/><stop offset=".6" stop-color="#f05a1e"/><stop offset="1" stop-color="#e3231c"/>
      </linearGradient>
      <linearGradient id="roomGrad" x1="0" y1="0" x2="1" y2="1">
        <stop offset="0" stop-color="#d9b77c"/><stop offset=".45" stop-color="#b58a55"/><stop offset="1" stop-color="#6e5236"/>
      </linearGradient>
    </defs>
    <path d="M0,432 C160,414 290,392 377,362 L377,740 L0,740 Z" fill="url(#roomGrad)" role="img" aria-label="Photo of the renovated reception and waiting area"/>
    <path d="M0,424 C230,400 430,320 560,240 C690,160 820,80 930,0 L990,0 C860,90 720,180 580,255 C420,340 220,410 0,432 Z" fill="url(#swooshGrad)"/>
    <path d="M560,232 C680,150 790,80 880,0 L905,0 C800,85 690,160 575,240 Z" fill="#c8dc2a"/>
    <path d="M0,700 C300,770 700,770 1128,630 L1128,800 L0,800 Z" fill="url(#bandGrad)"/>
    <path d="M120,745 C500,770 850,730 1128,660 L1128,680 C850,750 500,785 120,745 Z" fill="#e6f08a" opacity=".7"/>
    <path d="M400,97 Q400,62 435,60 L628,57 Q645,57 643,75 L637,150 Q635,170 615,170 L575,170 L560,190 L555,170 L420,170 Q403,170 402,150 Z" fill="url(#bubbleGrad)" stroke="#e3231c" stroke-width="3"/>
  </svg>

  <h2 class="abs heading about-title">About Us</h2>
  <p class="abs body-copy about-p1">Lorem ipsum dolor sit amet, consectetur adipisicing elit, sed do eiusmod tempor incididunt ut labore et dolore magna aliqua. Ut enim ad minim veniam, quis nostrud exercitation ullamco laboris nisi ut aliquip ex ea commodo consequat. Duis aute irure dolor in reprehenderit in voluptate velit esse cillum dolore eu fugiat nulla pariatur. Excepteur sint occaecat cupidatat non proident, sunt in culpa qui officia deserunt mollit anim id est laborum.</p>
  <p class="abs body-copy about-p2">Lorem ipsum dolor sit amet, consectetur adipisicing elit, sed do eiusmod tempor incididunt ut labore et dolore magna aliqua. Ut enim ad minim veniam, quis nostrud exercitation ullamco laboris nisi ut aliquip ex ea commodo consequat. Duis aute irure dolor in reprehenderit in voluptate velit esse cillum dolore eu fugiat nulla pariatur. Excepteur sint occaecat cupidatat non proident, sunt in culpa qui officia deserunt mollit anim id est laborum.</p>

  <p class="abs question-text">Are you worried about<br>your patient history?<br>We can help</p>

  <article class="doctor-card card-a">
    <div class="doctor-photo" role="img" aria-label="Portrait photo of Dr. Owen Hartley"></div>
    <div class="doctor-info">
      <h3 class="doctor-name">Dr. Owen Hartley</h3>
      <p class="doctor-bio">Lorem ipsum dolor sit amet, consectetur adipisicing elit, sed do eiusmod tempor incididunt ut labore et dolore magna aliqua. Ut enim ad minim veniam, quis nostrud exercitation ullamco laboris nisi ut aliquip ex ea commodo consequat.</p>
    </div>
  </article>

  <article class="doctor-card card-b">
    <div class="doctor-info">
      <h3 class="doctor-name">Dr. Selena</h3>
      <p class="doctor-bio">Lorem ipsum dolor sit amet, consectetur adipisicing elit, sed do eiusmod tempor incididunt ut labore et dolore magna aliqua. Ut enim ad minim veniam, quis nostrud exercitation ullamco laboris nisi ut aliquip ex ea commodo consequat.</p>
    </div>
    <div class="doctor-photo" role="img" aria-label="Portrait photo of Dr. Selena"></div>
  </article>

  <p class="abs body-copy middle-p">Lorem ipsum dolor sit amet, consectetur adipisicing elit, sed do eiusmod tempor incididunt ut labore et dolore magna aliqua. Ut enim ad minim veniam, quis nostrud exercitation ullamco laboris nisi ut aliquip ex ea commodo consequat. Duis aute irure dolor in reprehenderit in voluptate velit esse cillum dolore eu fugiat nulla pariatur. Excepteur sint occaecat cupidatat non proident, sunt in culpa qui officia deserunt mollit anim id est laborum.</p>

  <div class="abs brand">
    <span class="brand-mark"></span>
    <span class="brand-name">Tallowby Family Health</span>
  </div>

  <p class="abs tagline">MEDICAL | DENTAL</p>
  <h2 class="abs heading doctors-title">Our Friendly Doctors</h2>

  <article class="doctor-card card-c">
    <div class="doctor-photo" role="img" aria-label="Portrait photo of Dr. Owen Hartley"></div>
    <div class="doctor-info">
      <h3 class="doctor-name">Dr. Owen Hartley</h3>
      <p class="doctor-bio">Lorem ipsum dolor sit amet, consectetur adipisicing elit, sed do eiusmod tempor incididunt ut labore et dolore magna aliqua. Ut enim ad minim veniam, quis nostrud exercitation ullamco laboris nisi ut aliquip ex ea commodo consequat.</p>
    </div>
  </article>

  <h2 class="abs heading services-title">Other Services</h2>
  <p class="abs body-copy services-p">Lorem ipsum dolor sit amet, consectetur adipisicing elit, sed do eiusmod tempor incididunt ut labore et dolore magna aliqua. Ut enim ad minim veniam, quis nostrud exercitation ullamco laboris nisi ut aliquip ex ea commodo consequat.</p>
  <ul class="abs service-list">
    <li>PHYSIO</li>
    <li>PODIATRY</li>
    <li>PSYCHOLOGY</li>
    <li>DIETICIANS</li>
  </ul>

  <div class="abs magnet">MAGNET SPACE<br>for<br>BUSINESS CARD</div>
</main>
</body>
</html>
```